Single Page Timetracking Dashboard Desktop App UI Design (Figma Link required)

Main Idea: a SaaS tool where employees can add their time and project in a playful way. There is a infographics and a list with tasks as well.

Based on the attached concept.png the brief is following:

- check the attached rough scribble
- add own ideas or change things if they add value
- Style: colourful, nerdy, professional saas, modern, beautiful, white space
- Quality expectation: inspiration1+2.png
- I will need a Figma link
- desktop only
- make something fresh and unique

Process:
I need to include 2-3 feedback rounds that will span probably around 7 days

Target Market(s)

Internal Business Tool for a Software Development Company

Industry/Entity Type

IT

Other font styles liked:
• Could be monospace, not a must though

Requirements
Must have
• At least one page; Figma Link to the design;
Nice to have
• Microinterations like drop-down, hover/active colors; functionality specifications
Should not have
• Mobile view

```html
<!DOCTYPE html>
<html lang="en">
<head>
<meta charset="utf-8">
<title>Kivrel — Track your time</title>
<link rel="stylesheet" href="https://fonts.googleapis.com/css2?family=Open+Sans:wght@400;500;600;700&display=swap">
<style>
:root{
  --coral:#f58a87;
  --coral-soft:#f9a9a6;
  --amber:#fec04a;
  --amber-soft:#fcd89a;
  --sky:#5ccbeb;
  --sky-soft:#8fd9f0;
  --mint:#7fdc70;
  --mint-soft:#a6e59a;
  --ink:#2b2b2b;
  --text:#555;
  --muted:#8a8a8a;
  --line:#eeeeee;
  --panel:#ffffff;
  --tile:#fbfbfb;
}
*{box-sizing:border-box;margin:0;padding:0}
html,body{width:1200px;height:2558px;overflow:hidden}
body{font-family:"Open Sans",sans-serif;color:var(--ink);background:linear-gradient(180deg,#fd8a85 0%,#fea581 55%,#fec76f 100%);position:relative}
.abs{position:absolute}
.sidebar{position:absolute;left:0;top:0;width:155px;height:2558px;color:#fff}
.brand{position:absolute;left:0;width:140px;top:36px;text-align:center;font-weight:700;font-size:20px;letter-spacing:.5px}
.nav-item{position:absolute;left:14px;display:flex;align-items:center;gap:12px;font-size:15px;font-weight:500;color:#fff}
.nav-item.active{left:6px;width:149px;height:42px;padding-left:10px;background:rgba(255,255,255,.18);border-radius:21px 0 0 21px}
.main{position:absolute;left:155px;top:0;width:1045px;height:2558px;background:var(--panel);border-radius:40px 0 0 0}
.card{position:absolute;background:#fff;border-radius:6px;box-shadow:0 2px 14px rgba(0,0,0,.05)}
.tile{position:absolute;background:#fff;border-radius:5px;box-shadow:0 1px 6px rgba(0,0,0,.06)}
h1,h2{position:absolute;font-weight:700;font-size:28px;color:var(--ink)}
.btn-amber{position:absolute;background:var(--amber);color:#fff;border-radius:4px;font-weight:600;font-size:17px;display:flex;align-items:center;justify-content:center;gap:10px}
.cal-cell{position:absolute;width:28px;height:28px;margin-left:-14px;margin-top:-14px;display:flex;align-items:center;justify-content:center;font-size:13px;border-radius:50%}
.cal-head{font-weight:600}
.select{position:absolute;left:597px;width:242px;height:40px;font-size:12.5px;padding:0 18px;display:flex;align-items:center;justify-content:space-between;color:#444}
.person{position:absolute;left:597px;width:242px;height:44px;border-radius:4px;display:flex;align-items:center;font-size:12.5px;padding-left:12px}
.person .face{width:26px;height:26px;border-radius:50%;border:2px solid #fff;background:#b99c88;margin-right:8px}
.person .who{font-weight:600;width:106px}
.chip{position:absolute;width:60px;height:36px;border-radius:4px;display:flex;align-items:center;justify-content:center;font-size:15px;color:#777;background:#fff;box-shadow:0 1px 5px rgba(0,0,0,.07)}
.chip.on{background:var(--coral);color:#fff}
.label{position:absolute;font-size:18px;color:#444}
.stat-title{position:absolute;font-size:16px;color:#333}
.legend{position:absolute;font-size:13px;color:#555;line-height:29px}
.legend i{display:inline-block;width:9px;height:9px;border-radius:50%;margin:0 8px 0 12px}
.show-more{position:absolute;left:0;width:1200px;text-align:center;color:var(--coral);font-size:16px;text-decoration:underline;text-underline-offset:3px}
.day{position:absolute;left:228px;width:903px;display:flex;justify-content:space-between;font-size:16.5px}
.day b{font-weight:600}
.task{position:absolute;left:228px;width:903px;height:219px;background:#fff;border-radius:5px;box-shadow:0 1px 8px rgba(0,0,0,.06)}
.task .tag{position:absolute;left:28px;top:20px;font-size:13.5px;display:flex;align-items:center;gap:8px}
.tag.code{color:var(--coral)}
.tag.pm{color:#4ab54a}
.task .actions{position:absolute;right:30px;top:22px;display:flex;gap:30px;font-size:13.5px}
.actions .del{color:var(--amber)}
.actions .edit{color:#5aa7e0}
.task hr{position:absolute;left:12px;right:12px;top:54px;border:none;border-top:1px solid var(--line)}
.task .name{position:absolute;left:28px;top:75px;font-size:19px;color:#333}
.task .name span{margin-left:26px}
.task .desc{position:absolute;left:28px;top:116px;width:640px;font-size:14.5px;line-height:25.5px;color:var(--text)}
.task .meta{position:absolute;left:756px;top:80px;font-size:14.5px;color:#444;line-height:29px}
.meta div{display:flex;align-items:center;gap:8px}
</style>
</head>
<body>

<aside class="sidebar">
  <div class="brand">Kivrel</div>
  <div class="nav-item active" style="top:122px;">
    <svg width="20" height="20" viewBox="0 0 20 20"><circle cx="10" cy="11" r="7.5" fill="none" stroke="#fff" stroke-width="2"/><rect x="8" y="1" width="4" height="2" fill="#fff"/><path d="M10 11V7" stroke="#fff" stroke-width="2"/></svg>
    Track Time
  </div>
  <div class="nav-item" style="top:197px;">
    <svg width="20" height="20" viewBox="0 0 20 20"><rect x="1" y="9" width="4" height="9" fill="#fff"/><rect x="8" y="3" width="4" height="15" fill="#fff"/><rect x="15" y="7" width="4" height="11" fill="#fff"/></svg>
    Statistics
  </div>
  <div class="nav-item" style="top:263px;">
    <svg width="20" height="20" viewBox="0 0 20 20"><rect x="1" y="3" width="18" height="16" rx="2" fill="#fff"/><rect x="5" y="1" width="2" height="4" fill="#fff"/><rect x="13" y="1" width="2" height="4" fill="#fff"/><path d="M4 10l2 2 3-3M11 11h5M4 15h12" stroke="#fda080" stroke-width="1.6" fill="none"/></svg>
    Task
  </div>
  <div class="nav-item" style="top:329px;">
    <svg width="20" height="20" viewBox="0 0 20 20"><circle cx="10" cy="6" r="4.5" fill="#fff"/><path d="M2 19c0-5 3.5-7 8-7s8 2 8 7z" fill="#fff"/></svg>
    User
  </div>
  <div class="nav-item" style="top:2401px;">
    <svg width="20" height="20" viewBox="0 0 20 20"><path d="M2 2h9v16H2z" fill="#fff"/><path d="M12 10h7M16 6l4 4-4 4" stroke="#fff" stroke-width="2" fill="none"/></svg>
    Logout
  </div>
</aside>

<main class="main"></main>

<!-- top bar -->
<div class="tile" style="left:198px;top:30px;width:564px;height:44px;display:flex;align-items:center;font-size:13.5px;color:#999;">
  <div style="width:105px;padding-left:32px;border-right:1px solid var(--line);height:44px;display:flex;align-items:center;gap:6px;">Filter <svg width="8" height="5"><path d="M0 0l4 4 4-4" stroke="#aaa" fill="none"/></svg></div>
  <svg style="margin-left:24px" width="16" height="16" viewBox="0 0 16 16"><circle cx="7" cy="7" r="5.5" stroke="#999" stroke-width="1.4" fill="none"/><path d="M11 11l4 4" stroke="#999" stroke-width="1.4"/></svg>
  <span style="margin-left:10px;">Search</span>
  <svg style="margin-left:auto;margin-right:22px" width="12" height="12"><path d="M1 1l10 10M11 1L1 11" stroke="#999" stroke-width="1.4"/></svg>
</div>
<svg class="abs" style="left:975px;top:42px" width="20" height="20"><circle cx="10" cy="10" r="9" fill="#9a9a9a"/><text x="10" y="14.5" font-size="12" font-weight="700" fill="#fff" text-anchor="middle" font-family="Open Sans,sans-serif">?</text></svg>
<svg class="abs" style="left:1019px;top:42px" width="18" height="20"><path d="M9 1c-4 0-6 3-6 7v5l-2 3h16l-2-3V8c0-4-2-7-6-7z" fill="#9a9a9a"/><circle cx="9" cy="18" r="2" fill="#9a9a9a"/></svg>
<svg class="abs" style="left:1061px;top:42px" width="20" height="20"><path d="M10 2h8v16h-8" stroke="#9a9a9a" stroke-width="1.5" fill="none"/><path d="M1 10h11M8 6l4 4-4 4" stroke="#9a9a9a" stroke-width="1.5" fill="none"/></svg>
<div class="abs" role="img" aria-label="User profile photo" style="left:1118px;top:30px;width:44px;height:44px;border-radius:50%;border:3px solid #5cc15a;background:linear-gradient(135deg,#e6743c,#2f6e5c);"></div>

<h1 style="left:198px;top:116px;">Track your time</h1>

<!-- track card -->
<div class="card" style="left:198px;top:180px;width:965px;height:510px;"></div>
<div class="tile" style="left:228px;top:208px;width:359px;height:295px;"></div>
<svg class="abs" style="left:249px;top:232px" width="10" height="14"><path d="M8 1L2 7l6 6" stroke="#333" stroke-width="1.6" fill="none"/></svg>
<div class="abs" style="left:228px;top:226px;width:359px;text-align:center;font-size:18px;color:#333;">October, 2023</div>
<svg class="abs" style="left:555px;top:232px" width="10" height="14"><path d="M2 1l6 6-6 6" stroke="#333" stroke-width="1.6" fill="none"/></svg>

<div class="cal-cell cal-head" style="left:257px;top:284px">Su</div>
<div class="cal-cell cal-head" style="left:310px;top:284px">Mo</div>
<div class="cal-cell cal-head" style="left:357px;top:284px">Tu</div>
<div class="cal-cell cal-head" style="left:409px;top:284px">We</div>
<div class="cal-cell cal-head" style="left:457px;top:284px">Th</div>
<div class="cal-cell cal-head" style="left:505px;top:284px">Fr</div>
<div class="cal-cell cal-head" style="left:556px;top:284px">Sa</div>

<div class="cal-cell" style="left:257px;top:320px">01</div><div class="cal-cell" style="left:308px;top:320px">02</div><div class="cal-cell" style="left:357px;top:320px">03</div><div class="cal-cell" style="left:407px;top:320px">04</div><div class="cal-cell" style="left:457px;top:320px">05</div><div class="cal-cell" style="left:506px;top:320px">06</div><div class="cal-cell" style="left:556px;top:320px">07</div>
<div class="cal-cell" style="left:257px;top:357px">08</div><div class="cal-cell" style="left:308px;top:357px">09</div><div class="cal-cell" style="left:357px;top:357px">10</div><div class="cal-cell" style="left:407px;top:357px">11</div><div class="cal-cell" style="left:457px;top:357px;background:var(--coral);color:#fff;box-shadow:0 0 0 2px #fcd0cf">12</div><div class="cal-cell" style="left:506px;top:357px">13</div><div class="cal-cell" style="left:556px;top:357px">14</div>
<div class="cal-cell" style="left:257px;top:394px">15</div><div class="cal-cell" style="left:308px;top:394px">16</div><div class="cal-cell" style="left:357px;top:394px;background:var(--amber);box-shadow:0 0 0 2px #ffe3a8">17</div><div class="cal-cell" style="left:407px;top:394px">18</div><div class="cal-cell" style="left:457px;top:394px">19</div><div class="cal-cell" style="left:506px;top:394px;background:var(--sky);color:#fff;box-shadow:0 0 0 2px #bfe9f6">20</div><div class="cal-cell" style="left:556px;top:394px">21</div>
<div class="cal-cell" style="left:257px;top:431px">22</div><div class="cal-cell" style="left:308px;top:431px">23</div><div class="cal-cell" style="left:357px;top:431px">24</div><div class="cal-cell" style="left:407px;top:431px">25</div><div class="cal-cell" style="left:457px;top:431px">26</div><div class="cal-cell" style="left:506px;top:431px">27</div><div class="cal-cell" style="left:556px;top:431px">28</div>
<div class="cal-cell" style="left:257px;top:468px">29</div><div class="cal-cell" style="left:308px;top:468px">30</div><div class="cal-cell" style="left:357px;top:468px">31</div>

<div class="tile select" style="top:208px;">Select Project <svg width="9" height="5"><path d="M0 0l4.5 4 4.5-4" stroke="#777" fill="none"/></svg></div>
<div class="tile select" style="top:258px;">Select Type <svg width="9" height="5"><path d="M0 0l4.5 4 4.5-4" stroke="#777" fill="none"/></svg></div>

<div class="person" style="top:308px;background:var(--coral-soft);"><div class="face" role="img" aria-label="Team member photo"></div><span class="who">Nora Vance</span><span>3D Animation</span></div>
<div class="person" style="top:358px;background:var(--amber-soft);"><div class="face" role="img" aria-label="Team member photo" style="background:#6a5a50"></div><span class="who">Theo Marsh</span><span>UI/UX Design</span></div>
<div class="person" style="top:408px;background:var(--sky-soft);"><div class="face" role="img" aria-label="Team member photo" style="background:#d8b48e"></div><span class="who">Ivy Lund</span><span>App Design</span></div>
<div class="person" style="top:458px;background:var(--mint-soft);"><div class="face" role="img" aria-label="Team member photo" style="background:#a88a78"></div><span class="who">Owen Hale</span><span>App Design</span></div>

<div class="label" style="left:872px;top:202px;">Hours</div>
<div class="chip on" style="left:872px;top:239px">1h</div><div class="chip" style="left:938px;top:239px">2h</div><div class="chip" style="left:1005px;top:239px">3h</div><div class="chip" style="left:1071px;top:239px">4h</div>
<div class="chip" style="left:872px;top:283px">5h</div><div class="chip" style="left:938px;top:283px">6h</div><div class="chip" style="left:1005px;top:283px">7h</div><div class="chip" style="left:1071px;top:283px">8h</div>
<div class="label" style="left:872px;top:336px;">Minutes</div>
<div class="chip" style="left:872px;top:371px">10m</div><div class="chip on" style="left:938px;top:371px">15m</div><div class="chip" style="left:1005px;top:371px">30m</div><div class="chip" style="left:1071px;top:371px">45m</div>
<div class="tile" style="left:872px;top:430px;width:259px;height:73px;"></div>
<div class="abs" style="left:897px;top:453px;font-size:19px;font-weight:500;">1h 15m</div>
<div class="btn-amber" style="left:1066px;top:449px;width:44px;height:35px;"><svg width="12" height="15"><path d="M0 0h12v15l-6-4-6 4z" fill="#fff"/></svg></div>

<div class="tile" style="left:228px;top:518px;width:903px;height:141px;"></div>
<div class="abs" style="left:251px;top:542px;font-size:16px;color:#444;">What did you do?</div>

<!-- statistics -->
<h2 style="left:198px;top:748px;">Statistics</h2>
<div class="btn-amber" style="left:1047px;top:750px;width:116px;height:36px;">Month <svg width="11" height="7"><path d="M1 1l4.5 4.5L10 1" stroke="#fff" stroke-width="1.6" fill="none"/></svg></div>
<div class="card" style="left:198px;top:812px;width:965px;height:358px;"></div>

<div class="tile" style="left:228px;top:842px;width:435px;height:255px;"></div>
<div class="stat-title" style="left:249px;top:867px;">Current Month</div>
<div class="stat-title" style="left:521px;top:867px;">Total: <b style="font-weight:600">50:45 h</b></div>
<svg class="abs" style="left:249px;top:922px" width="138" height="138" viewBox="0 0 138 138">
  <g transform="rotate(-90 69 69)" fill="none" stroke-width="37">
    <circle cx="69" cy="69" r="50" stroke="#fdc862"/>
    <circle cx="69" cy="69" r="50" stroke="#f47f7f" stroke-dasharray="22 314.2" stroke-dashoffset="-160"/>
  </g>
</svg>
<div class="legend" style="left:437px;top:962px;">
  <div>40:45 h<i style="background:#fdc862"></i>Nora Vance (89%)</div>
  <div>10:00 h<i style="background:#f47f7f"></i>Theo Marsh (11%)</div>
</div>

<div class="tile" style="left:693px;top:842px;width:435px;height:255px;"></div>
<div class="stat-title" style="left:714px;top:867px;">September</div>
<div class="stat-title" style="left:985px;top:867px;">Total: <b style="font-weight:600">50:45 h</b></div>
<svg class="abs" style="left:713px;top:923px" width="138" height="138" viewBox="0 0 138 138">
  <g transform="rotate(-90 69 69)" fill="none" stroke-width="37">
    <circle cx="69" cy="69" r="50" stroke="#fdc862" stroke-dasharray="157.1 314.2"/>
    <circle cx="69" cy="69" r="50" stroke="#7fdc70" stroke-dasharray="7 314.2" stroke-dashoffset="-157.1"/>
    <circle cx="69" cy="69" r="50" stroke="#f47f7f" stroke-dasharray="15.7 314.2" stroke-dashoffset="-164.1"/>
    <circle cx="69" cy="69" r="50" stroke="#5ccbeb" stroke-dasharray="134.4 314.2" stroke-dashoffset="-179.8"/>
  </g>
</svg>
<div class="legend" style="left:902px;top:934px;">
  <div>40:45 h<i style="background:#fdc862"></i>Nora Vance (50%)</div>
  <div>08:15 h<i style="background:#f47f7f"></i>Theo Marsh (11%)</div>
  <div>20:00 h<i style="background:#5ccbeb"></i>Nora Vance (34%)</div>
  <div>22:45 h<i style="background:#7fdc70"></i>Theo Marsh (05%)</div>
</div>
<div class="show-more" style="top:1125px;left:80px;">Show More</div>

<!-- tasks -->
<h2 style="left:198px;top:1230px;">Your Tasks</h2>
<div class="btn-amber" style="left:1066px;top:1232px;width:97px;height:36px;">Filter <svg width="14" height="14"><path d="M0 0h14L8.5 7v7l-3-2V7z" fill="#fff"/></svg></div>
<div class="card" style="left:198px;top:1293px;width:965px;height:1202px;"></div>

<div class="day" style="top:1320px;"><span>Wednesday</span><b>07 hrs 30 min</b></div>

<div class="task" style="top:1367px;">
  <div class="tag code"><svg width="20" height="12"><path d="M5 1L1 6l4 5M15 1l4 5-4 5M12 0L8 12" stroke="#f58a87" stroke-width="1.5" fill="none"/></svg>Coding</div>
  <div class="actions"><span class="del">🗑 Delete</span><span class="edit">✎ Edit</span></div>
  <hr>
  <div class="name">Nora Vance<span>3D Animation</span></div>
  <div class="desc">Lorem ipsum dolor sit amet, consectetur adipiscing elit, sed do eiusmod tempo incididun ut labore et dolore magna aliqua. Ut enim ad minim veniam, quis nostrud exercitation ullamco laboris nisi ut aliquip ex ea commodo consequat.</div>
  <div class="meta"><div><svg width="13" height="13"><circle cx="6.5" cy="6.5" r="5.5" stroke="#f58a87" stroke-width="1.4" fill="none"/><path d="M6.5 3.5v3h2.5" stroke="#f58a87" stroke-width="1.3" fill="none"/></svg>4hrs 30mins</div><div><svg width="14" height="14"><rect x="1" y="2.5" width="12" height="10.5" rx="1" stroke="#fec04a" stroke-width="1.3" fill="none"/><path d="M1 6h12M4 0v4M10 0v4" stroke="#fec04a" stroke-width="1.3"/></svg>December 9th</div></div>
</div>

<div class="day" style="top:1626px;"><span>Tuesday</span><b>07 hrs 30 min</b></div>

<div class="task" style="top:1673px;">
  <div class="tag pm"><svg width="14" height="14"><circle cx="7" cy="7" r="5.5" stroke="#4ab54a" stroke-width="1.4" fill="none" stroke-dasharray="3 1.5"/><circle cx="7" cy="7" r="2" fill="#4ab54a"/></svg>Project Management</div>
  <div class="actions"><span class="del">🗑 Delete</span><span class="edit">✎ Edit</span></div>
  <hr>
  <div class="name">Owen Hale<span>App Design</span></div>
  <div class="desc">Lorem ipsum dolor sit amet, consectetur adipiscing elit, sed do eiusmod tempo incididun ut labore et dolore magna aliqua. Ut enim ad minim veniam, quis nostrud exercitation ullamco laboris nisi ut aliquip ex ea commodo consequat.</div>
  <div class="meta"><div><svg width="13" height="13"><circle cx="6.5" cy="6.5" r="5.5" stroke="#f58a87" stroke-width="1.4" fill="none"/><path d="M6.5 3.5v3h2.5" stroke="#f58a87" stroke-width="1.3" fill="none"/></svg>3hrs</div><div><svg width="14" height="14"><rect x="1" y="2.5" width="12" height="10.5" rx="1" stroke="#fec04a" stroke-width="1.3" fill="none"/><path d="M1 6h12M4 0v4M10 0v4" stroke="#fec04a" stroke-width="1.3"/></svg>December 9th</div></div>
</div>

<div class="task" style="top:1912px;">
  <div class="tag pm"><svg width="14" height="14"><circle cx="7" cy="7" r="5.5" stroke="#4ab54a" stroke-width="1.4" fill="none" stroke-dasharray="3 1.5"/><circle cx="7" cy="7" r="2" fill="#4ab54a"/></svg>Project Management</div>
  <div class="actions"><span class="del">🗑 Delete</span><span class="edit">✎ Edit</span></div>
  <hr>
  <div class="name">Nora Vance<span>App Design</span></div>
  <div class="desc">Lorem ipsum dolor sit amet, consectetur adipiscing elit, sed do eiusmod tempo incididun ut labore et dolore magna aliqua. Ut enim ad minim veniam, quis nostrud exercitation ullamco laboris nisi ut aliquip ex ea commodo consequat.</div>
  <div class="meta"><div><svg width="13" height="13"><circle cx="6.5" cy="6.5" r="5.5" stroke="#f58a87" stroke-width="1.4" fill="none"/><path d="M6.5 3.5v3h2.5" stroke="#f58a87" stroke-width="1.3" fill="none"/></svg>5hrs</div><div><svg width="14" height="14"><rect x="1" y="2.5" width="12" height="10.5" rx="1" stroke="#fec04a" stroke-width="1.3" fill="none"/><path d="M1 6h12M4 0v4M10 0v4" stroke="#fec04a" stroke-width="1.3"/></svg>December 9th</div></div>
</div>

<div class="task" style="top:2160px;">
  <div class="tag code"><svg width="20" height="12"><path d="M5 1L1 6l4 5M15 1l4 5-4 5M12 0L8 12" stroke="#f58a87" stroke-width="1.5" fill="none"/></svg>Coding</div>
  <div class="actions"><span class="del">🗑 Delete</span><span class="edit">✎ Edit</span></div>
  <hr>
  <div class="name">Nora Vance<span>3D Animation</span></div>
  <div class="desc">Lorem ipsum dolor sit amet, consectetur adipiscing elit, sed do eiusmod tempo incididun ut labore et dolore magna aliqua. Ut enim ad minim veniam, quis nostrud exercitation ullamco laboris nisi ut aliquip ex ea commodo consequat.</div>
  <div class="meta"><div><svg width="13" height="13"><circle cx="6.5" cy="6.5" r="5.5" stroke="#f58a87" stroke-width="1.4" fill="none"/><path d="M6.5 3.5v3h2.5" stroke="#f58a87" stroke-width="1.3" fill="none"/></svg>4hrs 30mins</div><div><svg width="14" height="14"><rect x="1" y="2.5" width="12" height="10.5" rx="1" stroke="#fec04a" stroke-width="1.3" fill="none"/><path d="M1 6h12M4 0v4M10 0v4" stroke="#fec04a" stroke-width="1.3"/></svg>December 9th</div></div>
</div>

<div class="show-more" style="top:2415px;left:80px;">Show More</div>

</body>
</html>
```